Entrepreneur needs a business card design

I need a business card to name my three companies, as well as contact information.
I'm open on design and color and it can be plain or complex. I'm open on colors but I think I prefer something somewhat formal but fun as well.
I'm open on whether the background is plain or has design in it. I don't have company logos.
Target Market(s)
Auto dealers, realtors and property managers
Industry/Entity Type
Business
Contact Information for Business Card
HOLLISTER FAMILY PROPERTIES, LLC
HOLLISTER PUBLISHING, LLC
LOTMASTER CONSULTING, LLC
Ned Hollister
2847 W. Tamarack Ave. #310
Boise, Idaho 83611-2905
208-514-3092
ned@holl5x.example

```html
<!DOCTYPE html>
<html lang="en">
<head>
<meta charset="UTF-8">
<title>Hollister Business Card</title>
<link rel="stylesheet" href="https://fonts.googleapis.com/css2?family=Cormorant+Garamond:wght@500;600&family=Source+Sans+3:wght@400&display=swap">
<style>
  :root {
    --navy: #2e4b69;
    --navy-line: rgba(255,255,255,0.45);
    --white: #ffffff;
    --page: #e9e9e7;
  }
  * { margin: 0; padding: 0; box-sizing: border-box; }
  html, body {
    width: 1200px; height: 900px; overflow: hidden;
    background: var(--page);
  }
  .card {
    position: absolute;
    left: 75px; top: 150px;
    width: 1050px; height: 600px;
    background: var(--white);
    box-shadow: 0 6px 24px rgba(0,0,0,0.18);
    overflow: hidden;
  }
  .company-block {
    position: absolute;
    left: 60px; top: 66px;
    width: 860px; height: 228px;
    background: var(--navy);
    display: flex; flex-direction: column;
    justify-content: center;
    padding-left: 40px;
  }
  .company-name {
    font-family: "Cormorant Garamond", "Times New Roman", serif;
    font-weight: 600;
    color: var(--white);
    font-size: 37px;
    letter-spacing: 1.5px;
    line-height: 1;
    padding: 10px 0;
    white-space: nowrap;
  }
  .company-name.indented { padding-left: 62px; }
  .company-divider {
    height: 1px;
    width: 520px;
    margin-left: 80px;
    background: linear-gradient(to right, transparent, var(--navy-line), transparent);
  }
  .person-name {
    position: absolute;
    left: 210px; top: 365px;
    font-family: "Source Sans 3", Arial, sans-serif;
    font-size: 34px;
    color: var(--navy);
    letter-spacing: 0.5px;
  }
  .contact-divider {
    position: absolute;
    left: 490px; top: 320px;
  }
  .contact-list {
    position: absolute;
    left: 545px; top: 330px;
    font-family: "Source Sans 3", Arial, sans-serif;
    font-size: 23px;
    color: var(--navy);
    line-height: 1.3;
    list-style: none;
    letter-spacing: 0.5px;
  }
  .address-band {
    position: absolute;
    left: 0; bottom: 0;
    width: 100%; height: 92px;
    background: var(--navy);
    display: flex; align-items: center;
    padding-left: 180px;
    font-family: "Source Sans 3", Arial, sans-serif;
    font-size: 26px;
    color: var(--white);
    letter-spacing: 0.5px;
  }
</style>
</head>
<body>
  <div class="card">
    <div class="company-block">
      <p class="company-name">HOLLISTER FAMILY PROPERTIES, LLC</p>
      <div class="company-divider"></div>
      <p class="company-name indented">HOLLISTER PUBLISHING, LLC</p>
      <div class="company-divider"></div>
      <p class="company-name indented">LOTMASTER CONSULTING, LLC</p>
    </div>

    <p class="person-name">Ned Hollister</p>

    <svg class="contact-divider" width="40" height="120" viewBox="0 0 40 120" aria-hidden="true">
      <line x1="4" y1="2" x2="34" y2="118" stroke="#2e4b69" stroke-width="1.5"/>
    </svg>

    <ul class="contact-list">
      <li>P : 208-514-3092</li>
      <li>E : ned@holl5x.example</li>
    </ul>

    <div class="address-band">2847 W. Tamarack Ave. #310 Boise, Idaho 83611-2905</div>
  </div>
</body>
</html>
```